Bramblewick Keystone

Looking for modern business cards.
Clean contemporary design.
Similar to this.
https://www.snapvorlo.net/imgview?src=https%3A%2F%2Fcdn.printquell.net%2Fprofessional_elegant_modern_black_plain_metal_business_card-a1b2c3d4e5f60718293a4b5c6d7e8f90_qwxyz_4tmpl_540.jpg&ref=https%3A%2F%2Fwww.printquell.net%2Fprofessional_elegant_modern_black_plain_metal_business_card-100200300400500600&id=7aB9cD3e-QR5TU&tid=Xyz_abc123defGH%3A&v=10abcDEFghiJKLmnoPQRstUVwxYZ0123456789abcd..x&w=540&h=540&bih=1360&biw=1061&q=modern%20business%20cards&ref2=0abcDEFghiJKLmnoPQRstUVwxYZ0123456789abcd&ia=mrc&ua=8

But I'd like the blue to look metallic.

```html
<!DOCTYPE html>
<html lang="en">
<head>
<meta charset="utf-8">
<title>Bramblewick Keystone — Business Card</title>
<link rel="stylesheet" href="https://fonts.googleapis.com/css2?family=Arimo:ital,wght@0,400;0,700;1,700&display=swap">
<style>
  :root {
    --page-bg: #e9e7e3;
    --card-grey: #e6e6ea;
    --card-panel: #f3f3f6;
    --teal: #1a8fb5;
    --navy: #1c4f6b;
    --navy-dark: #163f57;
    --ink: #222a30;
    --metal-deep: #0f6f95;
    --metal-mid: #2f95ba;
    --metal-light: #5fb4cf;
    --wordmark: #cfe7ef;
    --tagline: #f2f8fa;
  }
  * { box-sizing: border-box; margin: 0; padding: 0; }
  html, body {
    width: 1200px;
    height: 800px;
    overflow: hidden;
    background: var(--page-bg);
    font-family: "Arimo", Arial, sans-serif;
  }
  .sheet {
    width: 1200px;
    height: 800px;
    display: flex;
    align-items: center;
    justify-content: center;
    gap: 40px;
  }
  .card {
    position: relative;
    width: 540px;
    height: 309px;
    overflow: hidden;
    border-radius: 3px;
    box-shadow: 0 6px 18px rgba(0, 0, 0, 0.18);
  }

  /* Front: contact side */
  .card--front { background: var(--card-grey); }
  .card--front .panel {
    position: absolute;
    inset: 0;
    width: 100%;
    height: 100%;
  }
  .brand-front {
    position: absolute;
    top: 62px;
    right: 36px;
    display: flex;
    align-items: center;
    gap: 10px;
  }
  .brand-front .brand-name {
    font-size: 24px;
    font-weight: 700;
    color: var(--teal);
    white-space: nowrap;
  }
  .brand-front .brand-dot {
    width: 14px;
    height: 14px;
    border-radius: 50%;
    background: var(--navy);
  }
  .person {
    position: absolute;
    left: 40px;
    top: 112px;
  }
  .person .name {
    font-size: 27px;
    font-weight: 700;
    color: var(--teal);
    line-height: 1.05;
  }
  .person .role {
    font-size: 15px;
    color: var(--ink);
    margin-top: 2px;
  }
  .contact {
    position: absolute;
    left: 40px;
    bottom: 50px;
    list-style: none;
    font-size: 15px;
    color: var(--ink);
    line-height: 1.4;
  }

  /* Back: brand side, brushed metal */
  .card--back {
    background:
      repeating-linear-gradient(180deg,
        rgba(255,255,255,0.05) 0px, rgba(255,255,255,0.05) 1px,
        rgba(0,0,0,0.04) 2px, rgba(255,255,255,0) 3px),
      repeating-linear-gradient(178deg,
        rgba(255,255,255,0) 0px, rgba(255,255,255,0.07) 6px,
        rgba(255,255,255,0) 14px),
      linear-gradient(160deg,
        var(--metal-deep) 0%, var(--metal-mid) 32%,
        var(--metal-light) 50%, var(--metal-mid) 68%,
        var(--metal-deep) 100%);
  }
  .card--back::after {
    content: "";
    position: absolute;
    inset: 0;
    background: linear-gradient(115deg,
      rgba(255,255,255,0) 30%, rgba(255,255,255,0.16) 48%,
      rgba(255,255,255,0) 62%);
  }
  .brand-back {
    position: absolute;
    left: 0;
    right: 0;
    top: 118px;
    text-align: center;
    z-index: 1;
  }
  .brand-back .lockup {
    display: inline-flex;
    align-items: center;
    gap: 12px;
  }
  .brand-back .brand-name {
    font-size: 38px;
    font-weight: 400;
    color: var(--wordmark);
    letter-spacing: -0.5px;
    white-space: nowrap;
  }
  .brand-back .brand-dot {
    width: 16px;
    height: 16px;
    border-radius: 50%;
    background: var(--wordmark);
  }
  .tagline {
    margin-top: 8px;
    font-size: 11px;
    font-weight: 700;
    font-style: italic;
    letter-spacing: 1px;
    color: var(--tagline);
  }
</style>
</head>
<body>
<main class="sheet">

  <article class="card card--front">
    <svg class="panel" viewBox="0 0 540 309" preserveAspectRatio="none" aria-hidden="true">
      <polygon points="0,95 150,0 355,268 0,268" fill="var(--card-panel)"/>
      <rect x="0" y="268" width="540" height="5" fill="var(--teal)"/>
      <rect x="0" y="273" width="540" height="36" fill="var(--navy)"/>
      <rect x="0" y="301" width="540" height="8" fill="var(--navy-dark)"/>
    </svg>

    <div class="brand-front">
      <span class="brand-name">Bramblewick Keystone</span>
      <span class="brand-dot" aria-hidden="true"></span>
    </div>

    <div class="person">
      <p class="name">John Doe</p>
      <p class="role">Director</p>
    </div>

    <ul class="contact">
      <li>123 456 7890</li>
      <li>bramblewickkeystone.com</li>
      <li>email@bramblewickkeystone.com</li>
    </ul>
  </article>

  <article class="card card--back">
    <div class="brand-back">
      <div class="lockup">
        <span class="brand-name">Bramblewick Keystone</span>
        <span class="brand-dot" aria-hidden="true"></span>
      </div>
      <p class="tagline">“Steady Counsel for Every Stage of Growth”</p>
    </div>
  </article>

</main>
</body>
</html>
```